Business card and company stationary - Corvane Cleaning Ltd

1. Who are we and who are our customers?

o We are a relatively new cleaning company, established December 2008. We are a small company. We have 24 staff and we offer domestic and commercial cleaning services.
o We both (me and my wife) have been working for many years in the cleaning industry. We worked for some of the biggest and best cleaning companies in UK. We’ve been operatives, supervisors and managers.
o Inevitably after so many years of working for someone else, we decided to start our own business.
o Our domestic customers are middle class families and busy professionals. We’ve got some commercial customers, mainly offices.
o We are growing steadily.

2. What do we do? What are our services?

o Cleaning. We’ve got range of services - not to many but still can be daunting and confusing for some.
o Generally we’ve got domestic and commercial clients. The approach to the domestic cleaning customers is different to the commercial. In the way we want to say that it is cleaning that we do, but we acknowledge the environment and we appreciate the personal circumstances and requirements that are present. We do care, we listen and we try to work out the best possible way to complete our work.
o Mainly we get our work through referrals

3. What do we want with our stationery ?

o To place and maintain our message and reach out to people and organisations
o We want to advertise, communicate and sale.
o We are going to sell services.
o Increase membership, loyalty and support.

We are after business card design, headed letter and compliment slip.
We would like the headed letter to be created in formats suitable for :
- printing format
- also for use in our daily correspondence via e mail with clients and staff in a easy to edit and write format

The website we have is still under contraction and the domain is corvanecleaning.example

Target Market(s)

Families, individuals, businesses.

Industry/Entity Type

Cleaning Service

Contact Information for Business Card

FRONT :
Company Name - Corvane Cleaning Ltd
Company address - 41 Pelbury Rd, Pelbury, Essex, RM14 7QT
Name - Mrs. Teodora Vasilkova - Tedi
Title - Managing Director
Company phone - 020 8837 2591
E mail - tedi.vasilkova@corvanecleaning.example

BACK :

Company website - corvanecleaning.example
E mail - enquiries@corvanecleaning.example

Font styles to use
Serif

Requirements
Must have
• The above items and company logo...maybe at the back. But I'm free for any suggestions.

```html
<!DOCTYPE html>
<html lang="en">
<head>
<meta charset="utf-8">
<title>Corvane Cleaning Ltd – Business Card</title>
<link href="https://fonts.googleapis.com/css2?family=Source+Serif+4:wght@400;600;700&display=swap" rel="stylesheet">
<style>
  :root {
    --backdrop: #5a524e;
    --card: #141414;
    --card-edge: #1f1f1f;
    --accent: #3bb3e6;
    --ink: #f2f2f2;
    --ink-soft: #d4d4d4;
    --rule: #6b6b6b;
  }
  * { margin: 0; padding: 0; box-sizing: border-box; }
  html, body { width: 1200px; height: 814px; overflow: hidden; }
  body {
    background: var(--backdrop);
    font-family: "Source Serif 4", Georgia, serif;
    position: relative;
  }
  .card {
    position: absolute;
    width: 520px;
    height: 298px;
    background: var(--card);
    border: 1px solid var(--card-edge);
    top: 258px;
  }
  .card--front { left: 50px; }
  .card--back { left: 630px; }

  /* front */
  .brand {
    position: absolute;
    left: 20px; top: 58px;
    width: 200px;
    display: flex; flex-direction: column; align-items: center;
  }
  .brand__mark {
    width: 108px; height: 108px; border-radius: 50%;
    background: var(--ink);
    border: 4px solid var(--ink-soft);
  }
  .brand__name {
    margin-top: 20px;
    color: var(--accent);
    font-weight: 700;
    font-size: 19px;
    letter-spacing: 1.5px;
    text-transform: uppercase;
    text-align: center;
    line-height: 1.2;
  }
  .divider {
    position: absolute;
    left: 236px; top: 40px;
    width: 1px; height: 218px;
    background: var(--rule);
  }
  .details {
    position: absolute;
    left: 254px; top: 48px;
    width: 256px;
    color: var(--ink);
    font-size: 12px;
    line-height: 1.5;
  }
  .details__name {
    color: var(--accent);
    font-weight: 700;
    font-size: 15px;
    line-height: 1.25;
  }
  .details__title { margin-bottom: 10px; }
  .details__address { margin-bottom: 8px; }
  .contact { list-style: none; }
  .contact li { display: flex; align-items: center; gap: 7px; height: 20px; white-space: nowrap; }
  .contact svg { width: 11px; height: 11px; flex: none; fill: var(--accent); }

  /* back */
  .back__mark {
    position: absolute;
    left: 200px; top: 62px;
    width: 124px; height: 124px; border-radius: 50%;
    background: var(--ink);
    border: 4px solid var(--ink-soft);
  }
  .back__web {
    position: absolute;
    left: 0; right: 0; top: 214px;
    text-align: center;
    color: var(--ink);
    font-size: 12.5px;
    letter-spacing: 0.5px;
  }
</style>
</head>
<body>
  <section class="card card--front">
    <div class="brand">
      <div class="brand__mark"></div>
      <div class="brand__name">Corvane<br>Cleaning Ltd</div>
    </div>
    <div class="divider"></div>
    <div class="details">
      <div class="details__name">Mrs. Teodora Vasilkova - Tedi</div>
      <div class="details__title">Managing Director</div>
      <div class="details__address">41 Pelbury Rd, Pelbury,<br>Essex, RM14 7QT</div>
      <ul class="contact">
        <li><svg viewBox="0 0 12 12"><path d="M2.5 0.5l2 2.4-1.1 1.4a7 7 0 0 0 4.3 4.3l1.4-1.1 2.4 2-1.3 2A10 10 0 0 1 0.5 1.8z"/></svg>020 8837 2591</li>
        <li><svg viewBox="0 0 12 12"><path d="M0 2h12v1L6 7 0 3zM0 4.5l6 4 6-4V10H0z"/></svg>tedi.vasilkova@corvanecleaning.example</li>
        <li><svg viewBox="0 0 12 12"><path d="M0 2h12v1L6 7 0 3zM0 4.5l6 4 6-4V10H0z"/></svg>enquiries@corvanecleaning.example</li>
        <li><svg viewBox="0 0 12 12"><path d="M6 0a6 6 0 1 0 0 12A6 6 0 0 0 6 0zm0 1.5c1 1 1.5 2.6 1.6 3.8H4.4C4.5 4.1 5 2.5 6 1.5zM4.4 6.7h3.2C7.5 7.9 7 9.5 6 10.5 5 9.5 4.5 7.9 4.4 6.7z"/></svg>www.corvanecleaning.example</li>
      </ul>
    </div>
  </section>

  <section class="card card--back">
    <div class="back__mark"></div>
    <div class="back__web">www.corvanecleaning.example</div>
  </section>
</body>
</html>
```